Profesional personal website needs design and business card

I need a business card with my professional name as a logo "Orlan Vitality" for my business. I am a Wellness Coach, consultant and trainer. So it should be professional, wellness oriented and modern.

Target Market(s)

Private clients, governments, corporations. Luxury and high market.

Industry/Entity Type

Health And Wellness

Contact Information for Business Card

Orlan Vitality should be the logo

Colors

Designer to choose colors to be used in the design.

Requirements
Must have
• Orlan Vitality
• Name: Dario Montalbe
• Wellness Coach, Consultant & Trainer.
• Website: www.orlanvitality-example.com
• Phone:
• Spain (+34) 612 480 597
• (USA) +1 (555) 318 0264
Nice to have
• The most important is the design of "Orlan Vitality", as this is going to be my personal brand logo. It should be professional, wellness, high end and actual.
Should not have
• no golds, no baroque style..

```html
<!DOCTYPE html>
<html lang="en">
<head>
<meta charset="UTF-8">
<title>Orlan Vitality — Business Card</title>
<link href="https://fonts.googleapis.com/css2?family=Lato:wght@400;700;900&display=swap" rel="stylesheet">
<style>
  :root {
    --backdrop: #5b5b5b;
    --card-white: #ffffff;
    --card-black: #050607;
    --edge-blue: #1f78c8;
    --brand-blue: #1468bd;
    --ink-grey: #555a60;
    --logo-grey: #6b6d70;
  }
  * { margin: 0; padding: 0; box-sizing: border-box; }
  html, body {
    width: 1200px; height: 900px; overflow: hidden;
    background: var(--backdrop);
    font-family: "Lato", Arial, sans-serif;
  }
  .sheet {
    width: 1200px; height: 900px;
    display: flex; align-items: center; justify-content: center; gap: 50px;
  }
  .card {
    position: relative;
    width: 540px; height: 309px;
    border-radius: 2px;
    box-shadow: 0 10px 28px rgba(0,0,0,.35);
    overflow: hidden;
  }
  .card--front { background: var(--card-white); }
  .card--back {
    background: var(--card-black);
    border: 2px solid var(--edge-blue);
    display: flex; align-items: center; justify-content: center;
  }
  .brand {
    display: flex; align-items: center; gap: 10px;
    font-weight: 900; letter-spacing: -0.5px; text-transform: uppercase;
    white-space: nowrap;
  }
  .brand__dot { width: 14px; height: 14px; border-radius: 50%; flex: none; }
  .card--front .brand {
    position: absolute; left: 34px; top: 80px;
    color: var(--brand-blue); font-size: 22px;
  }
  .card--front .brand__dot { background: var(--brand-blue); width: 12px; height: 12px; }
  .card--back .brand { color: var(--logo-grey); font-size: 36px; }
  .card--back .brand__dot { background: var(--logo-grey); width: 20px; height: 20px; }
  .website {
    position: absolute; left: 34px; top: 176px;
    width: 212px; white-space: nowrap;
    font-size: 10.5px; letter-spacing: 1.5px; color: var(--ink-grey);
  }
  .website span { color: var(--brand-blue); }
  .divider {
    position: absolute; left: 262px; top: 140px;
    width: 1.5px; height: 96px; background: var(--brand-blue);
  }
  .details { position: absolute; left: 284px; top: 124px; right: 20px; }
  .details__name {
    font-size: 25px; font-weight: 900; color: var(--brand-blue);
    letter-spacing: -0.3px; text-transform: uppercase; line-height: 1;
    white-space: nowrap;
  }
  .details__role { font-size: 12px; color: var(--ink-grey); margin-top: 6px; white-space: nowrap; }
  .contacts { list-style: none; margin-top: 12px; }
  .contacts li {
    display: flex; align-items: center; gap: 8px;
    font-size: 12px; color: var(--ink-grey); line-height: 18px; white-space: nowrap;
  }
  .contacts svg { width: 12px; height: 12px; fill: var(--brand-blue); flex: none; }
</style>
</head>
<body>
<main class="sheet">
  <section class="card card--front" aria-label="Business card front">
    <div class="brand"><span class="brand__dot"></span>Orlan Vitality</div>
    <p class="website">www.<span>orlanvitality-example.com</span></p>
    <div class="divider"></div>
    <div class="details">
      <h1 class="details__name">Dario Montalbe</h1>
      <p class="details__role">Wellness Coach, Consultant &amp; Trainer</p>
      <ul class="contacts">
        <li><svg viewBox="0 0 24 24"><path d="M6.6 10.8a15.1 15.1 0 0 0 6.6 6.6l2.2-2.2c.3-.3.7-.4 1-.2 1.1.4 2.3.6 3.6.6.6 0 1 .4 1 1V20c0 .6-.4 1-1 1A17 17 0 0 1 3 4c0-.6.4-1 1-1h3.5c.6 0 1 .4 1 1 0 1.3.2 2.5.6 3.6.1.3 0 .7-.2 1z"/></svg>(+34) 612 480 597 (Spain)</li>
        <li><svg viewBox="0 0 24 24"><path d="M6.6 10.8a15.1 15.1 0 0 0 6.6 6.6l2.2-2.2c.3-.3.7-.4 1-.2 1.1.4 2.3.6 3.6.6.6 0 1 .4 1 1V20c0 .6-.4 1-1 1A17 17 0 0 1 3 4c0-.6.4-1 1-1h3.5c.6 0 1 .4 1 1 0 1.3.2 2.5.6 3.6.1.3 0 .7-.2 1z"/></svg>+1 (555) 318 0264 (USA)</li>
        <li><svg viewBox="0 0 24 24"><path d="M2 5h20v14H2z"/><path d="M3 6l9 7 9-7" fill="none" stroke="#fff" stroke-width="1.6"/></svg>info@orlanvitality-example.com</li>
      </ul>
    </div>
  </section>
  <section class="card card--back" aria-label="Business card back">
    <div class="brand"><span class="brand__dot"></span>Orlan Vitality</div>
  </section>
</main>
</body>
</html>
```